Business Card design for Founder and CEO of new shoe company

I am looking for a business card design for my new shoe company called Strapwell.

I am launching the company this April. Strapwell shoes offers slip-on athletic and casual style shoes for men and women. The unique selling point of the brand is that all of our shoe exist without shoelaces. I have included a link to the website to offer additional information about the company, see product images, and gain inspiration for the design. You can use the store owner password "Strapwell" to access the website.

www.Strapwell.example

Thanks,
Dan Hollis

Target Market(s)

Active Men and Women ages 16-45

Industry/Entity Type

Business

Contact Information for Business Card

Dan Hollis
Founder and CEO
www.Strapwell.example
danhollis@Strapwell.example
888-555-0187 / 888-5STRAPW
Strapwell, LLC
2284 N Tamsin Ave
Chicago, IL 60699

Requirements
Must have
• Be able to quickly and easily tell that Strapwell is a shoe company from the business card

```html
<!DOCTYPE html>
<html lang="en">
<head>
<meta charset="utf-8">
<title>Strapwell Business Card</title>
<link rel="stylesheet" href="https://fonts.googleapis.com/css2?family=Didact+Gothic&display=swap">
<style>
  :root {
    --page-bg: #d9d4cc;
    --card-white: #fbfbfb;
    --card-edge: #e6e6e6;
    --ink-gray: #8a8c90;
    --ink-dark: #6f7175;
    --brand-blue: #3f6ea6;
    --shoe-light: #b9babc;
    --shoe-mid: #8f9193;
    --shoe-dark: #6a6c6e;
    --accent-orange: #f0a35e;
  }
  * { margin: 0; padding: 0; box-sizing: border-box; }
  html, body {
    width: 733px; height: 1200px; overflow: hidden;
    background: var(--page-bg);
    font-family: "Didact Gothic", "Century Gothic", sans-serif;
  }
  .canvas { position: relative; width: 733px; height: 1200px; }
  .card {
    position: absolute; left: 56px; width: 620px; height: 354px;
    background: radial-gradient(ellipse at 40% 35%, #ffffff 0%, var(--card-white) 55%, #ececec 100%);
    border-radius: 22px;
    border: 1px solid var(--card-edge);
    box-shadow: 0 3px 0 #dcdcdc, 0 6px 0 #d2d2d2, 0 14px 28px rgba(0,0,0,0.18);
    overflow: hidden;
  }
  .card--front { top: 170px; }
  .card--back { top: 664px; }

  /* Front */
  .front-brand { position: absolute; left: 44px; top: 48px; }
  .wordmark {
    display: flex; align-items: center; gap: 10px;
    font-size: 44px; letter-spacing: 0.5px; line-height: 1;
  }
  .wordmark .mark-dot { width: 16px; height: 16px; border-radius: 50%; }
  .front-brand .wordmark { color: var(--ink-gray); }
  .front-brand .mark-dot { background: var(--ink-gray); }
  .front-brand .web {
    margin-top: 10px; margin-left: 26px;
    font-size: 14px; color: var(--ink-gray); letter-spacing: 0.3px;
  }
  .shoe-photo {
    position: absolute; right: 0; bottom: 0; width: 360px; height: 250px;
    background: linear-gradient(135deg, var(--accent-orange) 0%, var(--shoe-light) 28%, var(--shoe-mid) 65%, var(--shoe-dark) 100%);
    border-top-left-radius: 180px 140px;
  }

  /* Back */
  .back-brand { position: absolute; left: 44px; top: 40px; }
  .back-brand .wordmark { color: var(--brand-blue); font-size: 40px; }
  .back-brand .mark-dot { background: var(--brand-blue); }
  .contact-block { position: absolute; left: 44px; top: 150px; }
  .person-name { font-size: 32px; color: var(--ink-dark); line-height: 1.05; }
  .person-title { font-size: 15px; color: var(--brand-blue); margin-top: 4px; margin-bottom: 12px; }
  .contact-list { list-style: none; }
  .contact-list li {
    display: flex; align-items: flex-start; gap: 10px;
    font-size: 13px; color: var(--ink-gray); line-height: 1.4; margin-bottom: 4px;
  }
  .contact-list .icon { width: 14px; height: 14px; flex: 0 0 14px; margin-top: 2px; fill: var(--brand-blue); }
  .contact-list .web { color: var(--brand-blue); }
</style>
</head>
<body>
<div class="canvas">

  <section class="card card--front" aria-label="Business card front">
    <div class="front-brand">
      <div class="wordmark"><span class="mark-dot"></span>Strapwell</div>
      <div class="web">www.Strapwell.example</div>
    </div>
    <div class="shoe-photo" role="img" aria-label="Photo of a grey laceless athletic shoe with orange trim"></div>
  </section>

  <section class="card card--back" aria-label="Business card back">
    <div class="back-brand">
      <div class="wordmark"><span class="mark-dot"></span>Strapwell</div>
    </div>
    <div class="contact-block">
      <div class="person-name">Dan Hollis</div>
      <div class="person-title">Founder and CEO</div>
      <ul class="contact-list">
        <li>
          <svg class="icon" viewBox="0 0 16 16" aria-hidden="true"><path d="M1 3h14v10H1z M1 3l7 6 7-6" fill="none" stroke="#3f6ea6" stroke-width="1.6"/></svg>
          <span>danhollis@Strapwell.example</span>
        </li>
        <li>
          <svg class="icon" viewBox="0 0 16 16" aria-hidden="true"><path d="M4 1h3l1 4-2 1.5a9 9 0 0 0 3.5 3.5L11 8l4 1v3c0 1.5-1 3-3 3C6 15 1 10 1 4c0-2 1.5-3 3-3z"/></svg>
          <span>888-555-0187 / 888-5STRAPW</span>
        </li>
        <li>
          <svg class="icon" viewBox="0 0 16 16" aria-hidden="true"><path d="M8 0a5.5 5.5 0 0 0-5.5 5.5C2.5 10 8 16 8 16s5.5-6 5.5-10.5A5.5 5.5 0 0 0 8 0zm0 8a2.5 2.5 0 1 1 0-5 2.5 2.5 0 0 1 0 5z"/></svg>
          <span>Strapwell, LLC<br>2284 N Tamsin Ave<br>Chicago, IL 60699</span>
        </li>
        <li>
          <svg class="icon" viewBox="0 0 16 16" aria-hidden="true"><g fill="none" stroke="#3f6ea6" stroke-width="1.3"><circle cx="8" cy="8" r="6.5"/><ellipse cx="8" cy="8" rx="3" ry="6.5"/><path d="M1.5 8h13M2.5 4.5h11M2.5 11.5h11"/></g></svg>
          <span class="web">www.Strapwell.example</span>
        </li>
      </ul>
    </div>
  </section>

</div>
</body>
</html>
```